Actors Postcard Design

I need a postcard designed for me. I am an actor, voice over artist and technical adviser for tv, film and videogames. I am open to color ideas. My photos are in black and white so something to make those stand out a bit. Masculine colors like dark blue etc..I have seen some of your designs with 3 photos which I liked. Perhaps a 2-3 photo scheme. Back of postcard to contain my resume. Want it to look professional and not cartoonish (since I mentioned video games). Front to have photos and job title and contact info

Please take my color direction lightly, I am open to all color schemes. light or dark. You are the professionals. Am looking forward to seeing what all of you come up with. Thanks

Tv

```html
<!DOCTYPE html>
<html lang="en">
<head>
<meta charset="utf-8">
<title>Marek Kowalczyk – Actor Postcard</title>
<link rel="stylesheet" href="https://fonts.googleapis.com/css2?family=Michroma&family=Oswald:wght@600&family=Open+Sans:wght@400&family=Exo+2:wght@300&family=Parisienne&display=swap">
<style>
  :root{
    --bg:#1b1b1d;
    --ink:#0a0f16;
    --front-deep:#0c1a26;
    --photo-hi:#9cc7dc;
    --photo-mid:#3f7894;
    --photo-lo:#0f2433;
    --slate:#3d5463;
    --slate-dark:#2b3d4a;
    --band:#4d6b7c;
    --teal:#5fa8c2;
    --script:#7cc0d6;
    --white:#f4f8fa;
    --soft:#d7e3ea;
  }
  *{margin:0;padding:0;box-sizing:border-box}
  html,body{width:1200px;height:677px;overflow:hidden;background:var(--bg)}
  .canvas{position:relative;width:1200px;height:677px}

  /* FRONT */
  .front{position:absolute;left:12px;top:110px;width:590px;height:470px;background:var(--front-deep);overflow:hidden}
  .front .photo{position:absolute}
  .photo-left{left:0;top:0;width:150px;height:470px;background:linear-gradient(160deg,var(--photo-mid),var(--photo-lo) 80%)}
  .photo-right{right:0;top:0;width:150px;height:470px;background:linear-gradient(200deg,var(--photo-mid),var(--photo-lo) 80%)}
  .photo-main{left:95px;top:0;width:400px;height:470px;background:radial-gradient(ellipse at 50% 40%,var(--photo-hi) 0%,var(--photo-mid) 40%,var(--ink) 85%)}
  .front .frame{position:absolute;inset:0}
  .front .name{position:absolute;left:0;right:0;bottom:26px;text-align:center;font-family:"Michroma",sans-serif;font-size:19px;letter-spacing:4px;color:var(--white)}

  /* BACK */
  .back{position:absolute;left:614px;top:100px;width:574px;height:480px;background:var(--slate);overflow:hidden}
  .back .portrait{position:absolute;right:0;top:0;width:230px;height:480px;background:linear-gradient(180deg,#8fb4c4,#5c8799 70%,#4a7283)}
  .back .script-name{position:absolute;right:8px;top:345px;width:230px;text-align:center;font-family:"Parisienne",cursive;font-size:30px;line-height:1.15;color:var(--script)}
  .contact{position:absolute;left:0;top:20px;width:344px;height:80px;background:var(--slate-dark)}
  .contact .icons{position:absolute;left:8px;top:10px;display:flex;flex-direction:column;gap:18px}
  .contact .line{position:absolute;left:70px;font-family:"Exo 2",sans-serif;font-weight:300;color:var(--white);font-size:17px}
  .contact .phone{top:12px;left:130px}
  .contact .email{top:46px}
  .stats{position:absolute;left:0;top:110px;width:344px;height:26px;background:var(--band);font-family:"Parisienne",cursive;font-size:18px;color:var(--white);padding-left:10px;line-height:26px;white-space:nowrap}
  .resume{position:absolute;left:8px;top:146px;width:336px;display:flex;flex-direction:column;gap:8px}
  .entry{display:flex;gap:8px;height:76px}
  .thumb{width:60px;height:76px;flex:none;background:linear-gradient(160deg,#b9b9b9,#4a4a4a)}
  .entry-body{flex:1;background:var(--slate-dark);padding:4px 8px}
  .entry h2{font-family:"Oswald",sans-serif;font-weight:600;font-size:14px;color:var(--white);text-transform:uppercase;line-height:1.2}
  .entry p{font-family:"Open Sans",sans-serif;font-size:9.5px;line-height:1.3;color:var(--soft)}
</style>
</head>
<body>
<main class="canvas">

  <section class="front">
    <div class="photo photo-left" role="img" aria-label="Side headshot of the actor, blue tinted"></div>
    <div class="photo photo-right" role="img" aria-label="Side headshot of the actor smiling, blue tinted"></div>
    <div class="photo photo-main" role="img" aria-label="Main headshot of the actor in a plaid shirt, blue tinted"></div>
    <svg class="frame" width="590" height="470" viewBox="0 0 590 470" aria-hidden="true">
      <polyline points="110,40 88,60 140,255 70,440 90,470" fill="none" stroke="#ffffff" stroke-width="2"/>
      <polyline points="480,0 460,20 500,255 440,440 470,470" fill="none" stroke="#ffffff" stroke-width="2"/>
    </svg>
    <p class="name">MAREK “MARK” KOWALCZYK</p>
  </section>

  <section class="back">
    <div class="portrait" role="img" aria-label="Large faded headshot of the actor with halftone dots"></div>
    <p class="script-name">Marek<br>“Mark” Kowalczyk</p>

    <div class="contact">
      <div class="icons">
        <svg width="18" height="16" viewBox="0 0 18 16" aria-hidden="true"><path d="M3 1h3l1.5 4-2 1.5a9 9 0 0 0 5 5L12 9.5l4 1.5v3a2 2 0 0 1-2 2A13 13 0 0 1 1 3a2 2 0 0 1 2-2z" fill="none" stroke="#d7e3ea" stroke-width="1.3"/></svg>
        <svg width="18" height="14" viewBox="0 0 18 14" aria-hidden="true"><rect x="1" y="1" width="16" height="12" fill="none" stroke="#d7e3ea" stroke-width="1.3"/><path d="M1 1l8 7 8-7" fill="none" stroke="#d7e3ea" stroke-width="1.3"/></svg>
      </div>
      <p class="line phone">555-014-2290</p>
      <p class="line email">markkowalczyk@inboxmail.com</p>
    </div>

    <p class="stats">Height: 6'0" Weight: 180 Hair: Blond Eyes: Green</p>

    <div class="resume">
      <article class="entry">
        <div class="thumb" role="img" aria-label="Small black and white headshot"></div>
        <div class="entry-body">
          <h2>Acting</h2>
          <p>Elm Street Acting School – 1.5 yrs<br>Stage Forward Studio – On Camera 2yrs<br>Highland Acting Coach – 5 day intensive</p>
        </div>
      </article>
      <article class="entry">
        <div class="thumb" role="img" aria-label="Small black and white headshot"></div>
        <div class="entry-body">
          <h2>Voice Over</h2>
          <p>Voice Works – Daytime Conservatory (commercial, narration, etc…)<br>&nbsp;&nbsp;- Adv Daytime Conservatory<br>&nbsp;&nbsp;&nbsp;&nbsp;- 4 day Character Intensive</p>
        </div>
      </article>
      <article class="entry">
        <div class="thumb" role="img" aria-label="Small black and white headshot"></div>
        <div class="entry-body">
          <h2>Technical Advising</h2>
          <p>Federal Special Agent – 10.5 yrs<br>Extensive Firearms Training – Federal, Northline Tactics, Former Delta Members, Army ODA. Defensive Tactics, Breaching, Vehicle Containment, Surveillance, etc…</p>
        </div>
      </article>
      <article class="entry">
        <div class="thumb" role="img" aria-label="Small black and white headshot"></div>
        <div class="entry-body">
          <h2>Special Skills</h2>
          <p>15 yrs martial arts (Gung Fu, Judo, Tai Chi, Kenjutsu), EMT, Personal Trainer, Scuba, Snowboarding, Snowshoeing, Alpine Mountaineering, Archery, Mountainbiking, SUP, Blacksmithing, Carpentry 7yrs. Fluent Polish.</p>
        </div>
      </article>
    </div>
  </section>

</main>
</body>
</html>
```